PowerPoint Design Project

Hi,

Using our logo, we would like a designer to provide us with a powerpoint template that has a unique brand.

To us this means creating a color palette, treatment, a font that plays off of our logo. The color palette needs to blend well with our existing colors, but give us some options, make things "POP".

The color palette needs to include the colors (with RGB numbers), gradients, different graphic styles (solid, transparent, gradient, image fills) and lines (a callout leader line, a multi-color bar to divide content)

The palette and treatment must extend itself to graphs, charts and images.

We would also like to see different parts of our logo applied to the different template slides. For example, on a title slide we would like the image with our logo and tagline. With the end slide we would like to see our logo and URL. We also attached our logo without the tagline and also just the colored cube. So please be creative on how these are incorporated into the deck.

Images are attached.

Thank you
Carlton

Target Market(s)

Large Corporations

Requirements
Must have
• color palette, treatments and consistent fonts. color palette must complement our logo. color palette must extend to graphs, charts and images.

different logo's incorprated into the deck. For example, on a title slide we would like the image with our logo and tagline. With the end slide we would like to see our logo and URL. We also attached our logo without the tagline and also just the colored cube. So please be creative on how these are incorporated into the deck.
Should not have
• We do not want to see designers taking the logo and incorporating them into the background and calling it a template.

```html
<!DOCTYPE html>
<html lang="id">
<head>
<meta charset="utf-8">
<title>Title of Presentation</title>
<link href="https://fonts.googleapis.com/css2?family=Arimo&family=Carlito:wght@400;700&display=swap" rel="stylesheet">
<style>
  :root {
    --navy-deep: #0c1f3d;
    --navy: #163563;
    --navy-mid: #2c5a8e;
    --accent-green: #7cae2f;
    --slide-bg: #dfe5ee;
    --text-dark: #111826;
    --title-silver: #d6dce4;
    --seg-red: #a83a3a;
    --seg-red-side: #6e2020;
    --seg-teal: #2d6a74;
    --seg-teal-side: #173e45;
    --seg-green: #6f9231;
    --seg-green-side: #435c18;
    --seg-blue: #2b7cc7;
    --seg-blue-side: #174d82;
    --label-navy: #22395e;
    --brand-green: #79a934;
    --brand-dark: #1c2430;
  }
  * { margin: 0; padding: 0; box-sizing: border-box; }
  html, body { width: 1200px; height: 900px; overflow: hidden; }
  body { background: var(--slide-bg); font-family: "Arimo", Arial, sans-serif; }
  .slide { position: relative; width: 1200px; height: 900px; background: var(--slide-bg); overflow: hidden; }

  .header { position: absolute; left: 0; top: 0; width: 1200px; height: 88px; background: var(--navy-deep); }
  .header-panel {
    position: absolute; left: 232px; top: 0; width: 730px; height: 88px;
    background: linear-gradient(180deg, var(--navy-mid) 0%, var(--navy) 100%);
  }
  .header-corner { position: absolute; top: 0; width: 118px; height: 88px; background: linear-gradient(180deg, #13294b, #081730); }
  .header-corner.left { left: 0; }
  .header-corner.right { right: 0; }
  .corner-mark {
    position: absolute; top: 22px; width: 44px; height: 44px;
    background: linear-gradient(135deg, #5fa0d8, #2b6aa8);
  }
  .header-corner.left .corner-mark { left: 37px; }
  .header-corner.right .corner-mark { right: 37px; }
  .title-mark {
    position: absolute; top: 26px; width: 36px; height: 36px;
    background: linear-gradient(135deg, #8cbce6, #3d78b4);
  }
  .title-mark.left { left: 254px; }
  .title-mark.right { left: 910px; }
  .slide-title {
    position: absolute; left: 0; top: 14px; width: 1200px; text-align: center;
    font-family: "Carlito", Calibri, sans-serif; font-weight: 700; font-size: 56px; line-height: 60px;
    color: var(--title-silver); letter-spacing: 1px;
    text-shadow: 2px 2px 2px rgba(0,0,0,.75), -1px -1px 0 rgba(255,255,255,.25);
  }
  .header-rule { position: absolute; left: 0; top: 88px; width: 1200px; height: 11px; background: linear-gradient(180deg, var(--accent-green), #5f8c1f); }

  .cycle { position: absolute; left: 0; top: 0; width: 1200px; height: 900px; }

  .points { position: absolute; left: 0; top: 0; }
  .point { position: absolute; left: 546px; width: 600px; }
  .point-mark {
    position: absolute; left: 0; top: 4px; width: 24px; height: 24px;
    background: linear-gradient(135deg, var(--accent-green) 0%, #3d86c9 60%, #1c4f8a 100%);
  }
  .point p { margin-left: 59px; font-size: 22px; line-height: 31px; color: var(--text-dark); }
  .point.one { top: 182px; }
  .point.two { top: 348px; left: 555px; }
  .point.three { top: 477px; left: 548px; }
  .point.four { top: 645px; left: 558px; }

  .corner-deco {
    position: absolute; left: 1092px; top: 772px; width: 96px; height: 96px;
    background: linear-gradient(135deg, #b9d2dc, #8fb5c4); opacity: .6;
  }

  .brand { position: absolute; left: 0; top: 838px; width: 1200px; text-align: center; }
  .brand-name {
    font-family: "Arimo", Arial, sans-serif; font-weight: 700; font-size: 32px; line-height: 34px;
    color: var(--brand-green); letter-spacing: 1px;
  }
  .brand-url { font-size: 9px; line-height: 10px; color: #4a5a72; }
  .footer-rule { position: absolute; left: 0; top: 885px; width: 1200px; height: 15px; background: linear-gradient(180deg, var(--accent-green), #5f8c1f); }
</style>
</head>
<body>
<div class="slide">
  <header class="header">
    <div class="header-corner left"><span class="corner-mark"></span></div>
    <div class="header-panel"></div>
    <div class="header-corner right"><span class="corner-mark"></span></div>
    <span class="title-mark left"></span>
    <span class="title-mark right"></span>
    <h1 class="slide-title">Title of&nbsp; Presentation</h1>
  </header>
  <div class="header-rule"></div>

  <svg class="cycle" viewBox="0 0 960 720" width="1200" height="900" aria-label="Four-part cycle diagram">
    <defs>
      <radialGradient id="sphereFill" cx="38%" cy="30%" r="75%">
        <stop offset="0%" stop-color="#ffffff"/>
        <stop offset="45%" stop-color="#c9ccd1"/>
        <stop offset="85%" stop-color="#7c8088"/>
        <stop offset="100%" stop-color="#5b5f66"/>
      </radialGradient>
      <linearGradient id="redTop" x1="0" y1="0" x2="0" y2="1"><stop offset="0" stop-color="#c04848"/><stop offset="1" stop-color="#9a3030"/></linearGradient>
      <linearGradient id="tealTop" x1="0" y1="0" x2="1" y2="0"><stop offset="0" stop-color="#24565e"/><stop offset="1" stop-color="#3a7f8a"/></linearGradient>
      <linearGradient id="greenTop" x1="0" y1="0" x2="0" y2="1"><stop offset="0" stop-color="#7ea23a"/><stop offset="1" stop-color="#5e7f24"/></linearGradient>
      <linearGradient id="blueTop" x1="0" y1="0" x2="1" y2="0"><stop offset="0" stop-color="#3d93dc"/><stop offset="1" stop-color="#2466a8"/></linearGradient>
      <path id="arcRed" d="M143.4,287.1 A130,89 0 0 1 292.6,287.1"/>
      <path id="arcTeal" d="M292.6,287.1 A130,89 0 0 1 292.6,432.9"/>
      <path id="arcGreen" d="M143.4,432.9 A130,89 0 0 0 292.6,432.9"/>
      <path id="arcBlue" d="M143.4,432.9 A130,89 0 0 1 143.4,287.1"/>
    </defs>

    <g class="segment-sides" transform="translate(0,22)">
      <path fill="var(--seg-red-side)" d="M105.2,270.9 A172,118 0 0 1 330.8,270.9 L275.7,314.7 A88,60 0 0 0 160.3,314.7 Z"/>
      <path fill="var(--seg-teal-side)" d="M347.9,282.6 A172,118 0 0 1 347.9,437.4 L284.4,399.4 A88,60 0 0 0 284.4,320.6 Z"/>
      <path fill="var(--seg-green-side)" d="M330.8,449.1 A172,118 0 0 1 105.2,449.1 L160.3,405.3 A88,60 0 0 0 275.7,405.3 Z"/>
      <path fill="var(--seg-blue-side)" d="M88.1,437.4 A172,118 0 0 1 88.1,282.6 L151.6,320.6 A88,60 0 0 0 151.6,399.4 Z"/>
    </g>
    <g class="segment-tops">
      <path fill="url(#redTop)" d="M105.2,270.9 A172,118 0 0 1 330.8,270.9 L275.7,314.7 A88,60 0 0 0 160.3,314.7 Z"/>
      <path fill="url(#tealTop)" d="M347.9,282.6 A172,118 0 0 1 347.9,437.4 L284.4,399.4 A88,60 0 0 0 284.4,320.6 Z"/>
      <path fill="url(#greenTop)" d="M330.8,449.1 A172,118 0 0 1 105.2,449.1 L160.3,405.3 A88,60 0 0 0 275.7,405.3 Z"/>
      <path fill="url(#blueTop)" d="M88.1,437.4 A172,118 0 0 1 88.1,282.6 L151.6,320.6 A88,60 0 0 0 151.6,399.4 Z"/>
    </g>
    <g class="segment-labels" font-family="Carlito, Calibri, sans-serif" font-weight="700" font-size="21" fill="#ffffff" text-anchor="middle" dominant-baseline="middle" style="paint-order:stroke" stroke="rgba(0,0,0,.35)" stroke-width="1.5">
      <text><textPath href="#arcRed" startOffset="50%">Your text here</textPath></text>
      <text><textPath href="#arcTeal" startOffset="50%">Your text here</textPath></text>
      <text><textPath href="#arcGreen" startOffset="50%">Your text here</textPath></text>
      <text><textPath href="#arcBlue" startOffset="50%">Your text here</textPath></text>
    </g>

    <circle cx="216" cy="345" r="70" fill="url(#sphereFill)"/>
    <text x="216" y="348" text-anchor="middle" dominant-baseline="middle" font-family="Carlito, Calibri, sans-serif" font-weight="700" font-size="30" fill="var(--label-navy)">Label</text>
  </svg>

  <div class="points">
    <div class="point one"><span class="point-mark"></span><p>Janganlah kamu kuatir tentang apapun juga, tetapi nyatakanlah dalam segala hal keinginanmu kepada Tuhan dalam doa dan permohonan dengan ucapan syukur.</p></div>
    <div class="point two"><span class="point-mark"></span><p style="margin-left:51px">Percayalah kepada Tuhan&nbsp; dengansegenap hati dan pikiranmu dan janganlah bersandar kepada pengertianmu sendiri.</p></div>
    <div class="point three"><span class="point-mark"></span><p style="margin-left:58px">Janganlah kamu kuatir tentang apapun juga, tetapi nyatakanlah dalam segala hal keinginanmu kepada Tuhan dalam doa dan permohonan dengan ucapan syukur.</p></div>
    <div class="point four"><span class="point-mark"></span><p style="margin-left:51px">Percayalah kepada Tuhan&nbsp; dengansegenap hati dan pikiranmu dan janganlah bersandar kepada pengertianmu sendiri.</p></div>
  </div>

  <div class="corner-deco"></div>

  <div class="brand">
    <div class="brand-name">Veltrano</div>
    <div class="brand-url">www.veltrano.com</div>
  </div>
  <div class="footer-rule"></div>
</div>
</body>
</html>
```